web site to find a reliable, local tradesman, handyman or builder for any job

Design a web site as marketplace for handyman and client.
Handyman can
* set their profile (name, address, contacts)
* search / view / apply for job offers (by setting a new offer)
Client can
* search / view job offers
* generate new job offers (title, description, max price, date, duration, location).
* select and rate a job
Main functions would be SEARCH / VIEW to see in one glance WHAT needs to be done WHERE. The contractors then exchange contacts.
Handyman

```html
<!DOCTYPE html>
<html lang="en">
<head>
<meta charset="utf-8">
<title>Tradesfolk — Find a local handyman</title>
<link rel="stylesheet" href="https://fonts.googleapis.com/css2?family=PT+Sans:wght@400;700&family=Open+Sans:wght@600&family=Arimo:wght@400;700&family=Crimson+Text:wght@400&display=swap">
<style>
:root{
  --ink:#1c1c1c;
  --header-top:#343434;
  --header-bottom:#1b1b1b;
  --brand-red:#c10b0b;
  --nav-red-top:#c20c0c;
  --nav-red-bottom:#8e0404;
  --maroon:#5e0a0e;
  --gold:#f2b200;
  --panel-light:#e6e6e6;
  --panel-mid:#cfcfcf;
  --panel-dark:#0f0f0f;
  --field:#ffffff;
  --field-edge:#b9b9b9;
  --alert-red:#d40000;
  --orange-top:#ffc07a;
  --orange-bottom:#ee8a24;
  --quote-red:#7a0d12;
  --page:#ffffff;
}
*{box-sizing:border-box;margin:0;padding:0}
html,body{width:893px;height:1200px;overflow:hidden;background:var(--page)}
body{position:relative;font-family:"PT Sans",sans-serif;color:var(--ink)}
.abs{position:absolute}

.site-header{left:0;top:0;width:893px;height:102px;background:linear-gradient(var(--header-top),var(--header-bottom))}
.brand{left:42px;top:22px;font-family:"PT Sans",sans-serif;font-weight:700;font-size:46px;color:var(--brand-red);letter-spacing:-0.5px;line-height:1}

.main-nav{left:0;width:893px;height:31px;display:block}
.main-nav.top{top:102px;background:linear-gradient(var(--nav-red-top),var(--nav-red-bottom))}
.main-nav a{position:absolute;top:0;line-height:29px;transform:translateX(-50%);color:#fff;text-decoration:none;font-family:"Arimo",sans-serif;font-size:14px;white-space:nowrap}

.hero{left:0;top:133px;width:893px;height:332px;background:linear-gradient(90deg,#1e1e1e 0%,#2e2e2e 30%,#5a5a5a 55%,#7a7a7a 75%,#555 100%)}
.hero-copy{left:499px;top:176px;color:#fff;font-family:"Open Sans",sans-serif;font-weight:600;font-size:18.5px;line-height:24.5px;white-space:nowrap;letter-spacing:-0.1px}
.hero-dots span{position:absolute;top:430px;width:14px;height:14px;border-radius:50%;background:#111}
.hero-dots span.active{background:#a30d0d}
.hero-shadow{left:0;top:465px;width:893px;height:24px;background:radial-gradient(ellipse 450px 14px at 50% 0,rgba(0,0,0,.28),rgba(0,0,0,0))}

.section-title{font-family:"PT Sans",sans-serif;font-size:20px;font-weight:400;color:#111;white-space:nowrap;letter-spacing:.1px}

.search-band{left:37px;top:535px;width:811px;height:97px;background:var(--maroon);border-radius:8px}
.search-label{left:183px;top:561px;color:var(--gold);font-size:20px}
.field{position:absolute;background:var(--field);border-radius:9px;box-shadow:inset 0 3px 3px rgba(0,0,0,.35);border:1px solid var(--field-edge);font-family:"Arimo",sans-serif;font-size:11px;color:#b0b0b0;padding-left:12px;display:flex;align-items:center}
.btn-grey{position:absolute;border-radius:6px;background:linear-gradient(#f4f4f4,#c4c4c4);border:1px solid #9c9c9c;color:#8a8a8a;font-family:"Arimo",sans-serif;text-align:center}
.radio-opt{position:absolute;top:607px;display:flex;align-items:center;color:#fff;font-family:"Arimo",sans-serif;font-size:12px;white-space:nowrap}
.radio{display:inline-block;width:13px;height:13px;border-radius:50%;background:#fff;margin-right:7px}
.radio.on{background:radial-gradient(circle,#f2a100 0 3px,#fff 3.5px)}

.body-copy{font-family:"Crimson Text",serif;font-size:12.3px;line-height:21.5px;text-align:justify;color:#1a1a1a}
.body-copy .line{display:block;text-align:justify;text-align-last:justify;white-space:nowrap}
.body-copy .line.last{text-align-last:left}
.btn-more{position:absolute;width:64px;height:19px;border-radius:7px;background:linear-gradient(var(--orange-top),var(--orange-bottom));font-family:"Arimo",sans-serif;font-size:12px;color:#2a1a00;text-align:center;line-height:19px}
.photo-slot{position:absolute;border-radius:8px}

.panel-light{background:linear-gradient(var(--panel-light),var(--panel-mid));border-radius:8px}
.panel-dark{background:var(--panel-dark);border-radius:8px}
.forgot{font-family:"Arimo",sans-serif;font-size:10px;font-weight:700;color:var(--alert-red)}

.offer-label{position:absolute;left:605px;font-family:"Arimo",sans-serif;font-size:11px;color:#222}
.offer-colon{position:absolute;left:669px;font-family:"Arimo",sans-serif;font-size:11px;color:#222}
.offer-field{position:absolute;left:682px;width:160px;height:21px}

.testimonial{left:36px;top:1011px;width:541px;height:70px;border:1px solid #a8a8a8;border-radius:6px;background:linear-gradient(#f1f1f1,#cdcdcd)}
.quote-text{left:173px;top:1021px;width:340px;font-family:"Arimo",sans-serif;font-size:11px;line-height:22px;color:#1a1a1a}
.quote-mark{left:139px;top:1009px;font-family:"PT Sans",sans-serif;font-size:44px;font-weight:700;color:#c9c9c9;line-height:1}
.quote-by{left:454px;top:1055px;font-family:"Arimo",sans-serif;font-size:11px;color:var(--quote-red)}

.site-footer{left:0;top:1103px;width:893px;height:97px;background:linear-gradient(#2c2c2c,#1d1d1d)}
.main-nav.bottom{top:1111px}
.copyright{left:59px;top:1159px;font-family:"Arimo",sans-serif;font-size:10px;color:#fff}
.social{position:absolute;top:1155px;width:32px;height:32px;border-radius:50%;background:radial-gradient(circle at 40% 35%,#7fc1f3,#1f6bbd);box-shadow:0 2px 3px rgba(0,0,0,.6)}
</style>
</head>
<body>

<header class="site-header abs">
  <div class="brand abs">Tradesfolk</div>
</header>

<nav class="main-nav top abs">
  <a href="#" style="left:99px">Home</a>
  <a href="#" style="left:209px">About Us</a>
  <a href="#" style="left:334px">Apply for job</a>
  <a href="#" style="left:451px">Companies</a>
  <a href="#" style="left:572px">New jobs</a>
  <a href="#" style="left:667px">Search</a>
  <a href="#" style="left:784px">Contact Us</a>
</nav>

<section class="hero abs" role="img" aria-label="Photo: worker holding a hard hat in work gloves"></section>
<p class="hero-copy abs">Lorem Ipsum is simply dummy text of<br>the printing and typesetting industry.<br>Lorem Ipsum has been the industry's<br>standard dummy text</p>
<div class="hero-dots">
  <span style="left:691px"></span><span style="left:709px"></span><span class="active" style="left:727px"></span>
</div>
<div class="hero-shadow abs"></div>

<h1 class="section-title abs" style="left:41px;top:494px">Welcome to Our website</h1>

<form class="search-band abs"></form>
<div class="search-label abs">Search</div>
<div class="field" style="left:259px;top:560px;width:340px;height:31px"></div>
<div class="btn-grey" style="left:609px;top:562px;width:88px;height:27px;font-size:16px;line-height:25px">Search</div>
<label class="radio-opt" style="left:271px"><span class="radio on"></span>Handyman</label>
<label class="radio-opt" style="left:368px"><span class="radio"></span>Constructor</label>
<label class="radio-opt" style="left:465px"><span class="radio"></span>Builders</label>

<h2 class="section-title abs" style="left:39px;top:651px">Company Profile</h2>
<div class="photo-slot" style="left:37px;top:691px;width:190px;height:129px;background:linear-gradient(135deg,#7fa9d6 0%,#a9c7e4 50%,#cfc9bb 100%)" role="img" aria-label="Photo: handshake in front of a construction site"></div>
<p class="body-copy abs" style="left:245px;top:687px;width:320px">Lorem ipsum dolor sit amet, consectetur adipisicing elit, sed do eiusmod tempor incididunt ut labore et dolore magna aliqua. Ut enim ad minim veniam, quis nostrud exercitation ullamco laboris nisi ut aliquip ex ea commodo consequat. Duis aute irure dolor in reprehenderit in voluptate velit esse cillum....</p>
<div class="btn-more" style="left:495px;top:781px">More...</div>

<h2 class="section-title abs" style="left:614px;top:646px">User Login</h2>
<div class="panel-light abs" style="left:596px;top:675px;width:256px;height:129px"></div>
<div class="field" style="left:607px;top:687px;width:232px;height:30px">Username</div>
<div class="field" style="left:607px;top:733px;width:234px;height:30px">Password</div>
<div class="forgot abs" style="left:618px;top:778px">Forgot password ?</div>
<div class="btn-grey" style="left:766px;top:772px;width:66px;height:21px;font-size:12px;line-height:19px">Login</div>

<h2 class="section-title abs" style="left:39px;top:829px">Member Login</h2>
<div class="panel-dark abs" style="left:37px;top:863px;width:256px;height:130px"></div>
<div class="field" style="left:49px;top:875px;width:232px;height:30px">Username</div>
<div class="field" style="left:49px;top:920px;width:234px;height:31px">Password</div>
<div class="forgot abs" style="left:59px;top:966px">Forgot password ?</div>
<div class="btn-grey" style="left:207px;top:961px;width:66px;height:21px;font-size:12px;line-height:19px">Login</div>

<h2 class="section-title abs" style="left:358px;top:829px">Need a Handyman?</h2>
<p class="body-copy abs" style="left:332px;top:873px;width:231px">
  <span class="line">Lorem ipsum dolor sit amet, consectetur adipi-</span>
  <span class="line">sicing elit, sed do eiusmod tempor incididunt ut</span>
  <span class="line">labore et dolore magna aliqua. Lorem ipsum</span>
  <span class="line">dolor sit amet, consectetur adipisicing elit,</span>
  <span class="line last">dolore magna aliqua.</span>
</p>
<div class="btn-more" style="left:495px;top:972px">More...</div>

<h2 class="section-title abs" style="left:606px;top:824px">Generate New Job Offers</h2>
<div class="panel-light abs" style="left:597px;top:862px;width:256px;height:219px"></div>
<span class="offer-label" style="top:879px">Title</span><span class="offer-colon" style="top:879px">:</span><div class="field offer-field" style="top:875px"></div>
<span class="offer-label" style="top:908px">Description</span><span class="offer-colon" style="top:908px">:</span><div class="field offer-field" style="top:905px"></div>
<span class="offer-label" style="top:936px">Max Price</span><span class="offer-colon" style="top:936px">:</span><div class="field offer-field" style="top:934px"></div>
<span class="offer-label" style="top:964px">Date</span><span class="offer-colon" style="top:964px">:</span><div class="field offer-field" style="top:963px"></div>
<span class="offer-label" style="top:993px">Duration</span><span class="offer-colon" style="top:993px">:</span><div class="field offer-field" style="top:992px"></div>
<span class="offer-label" style="top:1021px">Location</span><span class="offer-colon" style="top:1021px">:</span><div class="field offer-field" style="top:1020px"></div>
<div class="btn-grey" style="left:686px;top:1069px;width:98px;height:21px;font-size:14px;line-height:20px;color:#1a1a1a">Generate</div>

<blockquote class="testimonial abs"></blockquote>
<div class="photo-slot" style="left:72px;top:1016px;width:52px;height:58px;background:linear-gradient(#c9c9c9,#8fb4d8)" role="img" aria-label="Member avatar"></div>
<div class="quote-mark abs">“</div>
<p class="quote-text abs">Lorem ipsum dolor sit amet, consectetur adipisicing elit, sed do eius-mod tempor incididunt</p>
<div class="quote-by abs">Milo &nbsp;- 12-Nov-2011</div>

<footer class="site-footer abs"></footer>
<nav class="main-nav bottom abs">
  <a href="#" style="left:79px">Home</a>
  <a href="#" style="left:189px">About Us</a>
  <a href="#" style="left:314px">Apply for job</a>
  <a href="#" style="left:432px">Companies</a>
  <a href="#" style="left:552px">New jobs</a>
  <a href="#" style="left:647px">Search</a>
  <a href="#" style="left:765px">Contact Us</a>
</nav>
<div class="copyright abs">Copyright © 2011.www.tradesfolk-hub.com</div>
<span class="social" style="left:724px" aria-label="Social profile"></span>
<span class="social" style="left:766px" aria-label="Social profile"></span>

</body>
</html>
```